Business card with logo for a family psychologist

I need a business card for my private practice in the urban Chicago area as a psychologist. I see families and individuals who are going through difficult times - divorce, separation, illness, or trauma. I want to project hopefulness, competence, and caring.

Target Market(s)

Adults, other professionals - such as physicans and lawyers

Industry/Entity Type

Health Care

Contact Information for Business Card

Front should have my name and credentials; back should have location information including my email, phone

Font styles to use
Serif
Decorative
Script

Requirements
Must have
• Unique logo
Should not have
• No pictures or icons of people; no black

```html
<!DOCTYPE html>
<html lang="en">
<head>
<meta charset="utf-8">
<title>Dana Whitfield, Ph.D. – Business Card</title>
<link rel="stylesheet" href="https://fonts.googleapis.com/css2?family=Tinos:wght@400&display=swap">
<style>
  :root {
    --backdrop: #dcd8d0;
    --card-plum: #8a0d5c;
    --accent-gold: #e8c98c;
    --text-white: #ffffff;
  }
  html, body {
    margin: 0;
    padding: 0;
    width: 1078px;
    height: 1200px;
    overflow: hidden;
    background: var(--backdrop);
  }
  .stage {
    position: relative;
    width: 1078px;
    height: 1200px;
    font-family: "Tinos", "Times New Roman", serif;
  }
  .card {
    position: absolute;
    left: 149px;
    width: 780px;
    height: 460px;
    border-radius: 34px;
    background: var(--card-plum);
    overflow: hidden;
  }
  .card-front { top: 131px; }
  .card-back  { top: 645px; }

  .logo-mark {
    position: absolute;
    border-radius: 50%;
    background: var(--accent-gold);
  }
  .card-front .logo-mark { left: 244px; top: 109px; width: 104px; height: 104px; }
  .card-back .logo-mark  { left: 147px; top: 76px;  width: 100px; height: 100px; }

  .practice-name {
    position: absolute;
    margin: 0;
    color: var(--accent-gold);
    font-weight: 400;
    font-size: 30px;
    line-height: 1;
    white-space: nowrap;
  }
  .card-front .practice-name { left: 283px; top: 232px; }
  .card-back .practice-name  { left: 283px; top: 102px; }

  .divider {
    position: absolute;
    left: 0;
    top: 278px;
    width: 100%;
    height: 4px;
    background: var(--accent-gold);
  }
  .title {
    position: absolute;
    margin: 0;
    color: var(--text-white);
    font-size: 23px;
    letter-spacing: 0.2px;
    line-height: 1;
    white-space: nowrap;
  }
  .card-front .title { left: 0; width: 780px; text-align: center; top: 294px; }
  .card-back .title  { left: 285px; top: 150px; font-size: 20.5px; }

  .contact-rail {
    position: absolute;
    left: 170px;
    top: 0;
    width: 50px;
    height: 460px;
  }
  .contact-list {
    position: absolute;
    left: 232px;
    top: 200px;
    margin: 0;
    padding: 0;
    list-style: none;
    color: var(--text-white);
    font-size: 27px;
    line-height: 33px;
  }
  .contact-list li { margin: 0; }
  .contact-address { height: 66px; margin-bottom: 18px !important; }
  .contact-phone   { margin-bottom: 23px !important; }
</style>
</head>
<body>
<main class="stage">

  <section class="card card-front" aria-label="Card front">
    <div class="logo-mark" aria-hidden="true"></div>
    <h1 class="practice-name">Dana Whitfield, Ph.D.</h1>
    <div class="divider"></div>
    <p class="title">LICENSED CLINICAL PSYCHOLOGIST</p>
  </section>

  <section class="card card-back" aria-label="Card back">
    <div class="logo-mark" aria-hidden="true"></div>
    <h2 class="practice-name">Dana Whitfield, Ph.D.</h2>
    <p class="title">LICENSED CLINICAL PSYCHOLOGIST</p>

    <svg class="contact-rail" viewBox="0 0 50 460" aria-hidden="true">
      <line x1="25" y1="170" x2="25" y2="460" stroke="#e8c98c" stroke-width="4"/>
      <!-- location -->
      <circle cx="25" cy="232" r="17" fill="#8a0d5c" stroke="#e8c98c" stroke-width="3"/>
      <path d="M25 242 C19 234 18 230 18 227 a7 7 0 0 1 14 0 c0 3 -1 7 -7 15z" fill="none" stroke="#e8c98c" stroke-width="2.2"/>
      <circle cx="25" cy="227" r="2.6" fill="#e8c98c"/>
      <!-- phone -->
      <circle cx="25" cy="298" r="17" fill="#8a0d5c" stroke="#e8c98c" stroke-width="3"/>
      <path d="M19 290 l4 -1 2 5 -3 2 c1 3 3 5 6 6 l2 -3 5 2 -1 4 c-8 1 -16 -7 -15 -15z" fill="none" stroke="#e8c98c" stroke-width="2"/>
      <!-- mail -->
      <circle cx="25" cy="353" r="17" fill="#8a0d5c" stroke="#e8c98c" stroke-width="3"/>
      <rect x="15" y="346" width="20" height="14" rx="2" fill="none" stroke="#e8c98c" stroke-width="2"/>
      <path d="M15 347 L25 355 L35 347" fill="none" stroke="#e8c98c" stroke-width="2"/>
    </svg>

    <ul class="contact-list">
      <li class="contact-address">240 W. Harlow Suite 815<br>Chicago, Illinois 60610</li>
      <li class="contact-phone">312-555-0148</li>
      <li class="contact-email">Drdanawhitfield@mailbox.com</li>
    </ul>
  </section>

</main>
</body>
</html>
```